Colourful Bold Design for Pet Insurance Website

PLEASE NOTE THAT THIS PROJECT HAS BEEN EXTENDED. Please read the PROJECT EXTENSION DOCUMENT BEFORE STARTING WORK ON ANY DESIGNS.

We are looking for a colourful bold new template design for our JOOMLA HOMEPAGE and a matching design for our new WORDPRESS BLOG.

The website will help pet owners work out which insurance policy best meets their needs. The aim of the website is to explain policy differences in a plain clear manner.

The website will need to have a professional colourful image. It needs to be BOLD, CLEAN AND SHARP rather than soft, pastel and cuddly.

COLOUR SCHEME
The website needs to have a bold colourful design on a white background.
On the inner pages we will have five different types of policies which will be colour coded. We would ideally therefore like to incorporate five distinct colours in the design. See attached document for example of colour schemes we like.

LOGO
We want to keep the existing logo. Please find the file attached. You may though change the logo colours.

CONTENT
One of the reasons for the new design is that we want to change the style of the homepage and include new content. Our current homepage can be found at www.cover-compare-quizzo.co.uk.

Content Required
Slideshow
Article Intro.. About Pet Insurance
Policy Lookup Box (see existing site… you can change the design of this)
Six link options (see links on left of current page)
Latest Reviews (List of 6)
Ad (Same dimensions as currently on homepage)

News and Comment Section - To include Three or Four Articles, Title, Intro to article (probably 3 or 4 lines .. about 400px wide), Read more link
Social Media Section
plain square Plugin with Feed
Latest Tweets Plugin
Pet Charities Latest Tweets
Footer
Larger footer with lots of links grouped in sections

It does not need to include the clipart pic of the pets which is on the current homepage.

Examples of Websites and Templates We Like
http://www.brindlevox.com/ (like colours… fonts…layout)
http://layoutdemo.quarnofield.com/?template=elated&path=/... (like the clarity, "white" space etc)
http://www.skellpravo.com/demo/58817.html (like white space, clear easy to read fonts… don’t like colour scheme, size of top picture)
http://www.skellpravo.com/website-templates/62391.html (like colour scheme, use of white space)

FEEDBACK
I will provide lots of feedback on all designs submitted so that together we can get the best result.

For clarification this is a DESIGN ONLY project. Our website developer will view the designs before we make our final choice as he wants to ensure he can develop "sharp, practical and most importantly light weight web interface" from the design.

Just updated this brief to clarify design issues, content issues and to give some more examples of site designs I like. 

Please note that although we wish to keep the logo you can change the colours to suit your design. 

Please note that we have now added details of pictures we would be happy to use on the website.  We would prefer it if you used one of these.   Otherwise please ensure your picture includes a nice dog and nice cat and no people!

I have been delighted with the quality of the designs submitted for this project.  So much so that I am going to extend the project to include some additional inner pages.   The amended brief will be posted on here on Friday 10 May.   The deadline will be extended and the budget will also be increased. 

Reason: Additional inner pages now required. Budget will be increased. Revised brief to be posted on here Friday 10 May.

Target Market(s)

Pet owners in the UK who are confused about pet insurance. It therefore needs to be a bold design which is plain, clean and easy to read. It should use bold colours rather than pastels and should not use "cuddly" images.

Industry/Entity Type

Insurance

Requirements
Must have
• Bold clear and distinct colours (preferably 5)
Content as per uploaded file (not just content from existing site)
Easy to read fonts
Should not have
• Pastel colours
Cuddly images

```html
<!DOCTYPE html>
<html lang="en">
<head>
<meta charset="utf-8">
<title>Cover Compare Quizzo</title>
<link href="https://fonts.googleapis.com/css2?family=Roboto+Condensed:wght@300;400;700&family=Arimo:wght@400;700&display=swap" rel="stylesheet">
<style>
:root{
  --bg:#f3f3f3;
  --white:#ffffff;
  --ink:#555;
  --ink-dark:#333;
  --orange:#f07c1d;
  --pink:#e6168f;
  --green:#3f8a52;
  --green-light:#5cbf72;
  --blue:#1480cf;
  --steel:#6d97c9;
  --panel:#e5e5e5;
  --footer:#e2e2e2;
}
*{margin:0;padding:0;box-sizing:border-box}
html,body{width:900px;height:1200px;overflow:hidden}
body{background:var(--bg);font-family:Arimo,Arial,sans-serif;color:var(--ink);position:relative}
.abs{position:absolute}
.cond{font-family:"Roboto Condensed",Arial,sans-serif}

.logo{left:74px;top:14px;width:162px;height:83px;background:#000;border:3px solid #fff;box-shadow:0 1px 3px rgba(0,0,0,.3);display:flex;align-items:center;justify-content:center;gap:8px}
.logo-mark{width:22px;height:22px;background:var(--steel)}
.logo-name{color:#fff;font:700 15px/1.1 Arimo,Arial,sans-serif;width:100px}

.nav{left:314px;top:26px;width:511px;height:62px;background:var(--white);border-top:4px solid #ddd;display:flex;align-items:center;justify-content:space-around;box-shadow:0 8px 6px -6px rgba(0,0,0,.2)}
.nav a{font-size:11.5px;color:var(--ink-dark);text-decoration:none}
.nav .active-bar{position:absolute;left:0;top:-4px;width:60px;height:4px;background:var(--orange)}

.hero-text{left:76px;top:176px;line-height:1}
.hero-text .l1{font-size:24px;color:#666;font-weight:700}
.hero-text .l1 b{font-size:44px;color:var(--orange)}
.hero-text .l2{font-size:45px;color:var(--pink);font-weight:700;margin-top:2px}
.hero-text .l3{font-size:40px;color:#777;font-weight:300;margin-top:2px}
.hero-photo{left:512px;top:128px;width:312px;height:192px;background:radial-gradient(ellipse at 50% 55%,#8a7560 0%,#c9bfb3 45%,rgba(243,243,243,0) 72%)}
.slider-arrows{left:772px;top:138px;width:54px;height:29px;background:var(--green-light);display:flex}
.slider-arrows span{flex:1;display:flex;align-items:center;justify-content:center}
.slider-arrows span+span{border-left:1px solid rgba(255,255,255,.5)}

.lookup{left:0;top:332px;width:900px;height:114px;background:var(--blue)}
.lookup h2{position:absolute;left:76px;top:10px;color:#fff;font-size:24px;font-weight:700;display:flex;align-items:center;gap:8px}
.lookup-icon{width:18px;height:30px;background:#1a2a55;border-radius:3px}
.select{position:absolute;top:50px;width:280px;height:50px;border:1px solid #8fc3ec;padding:4px}
.select div{height:100%;background:#e4e4e4;border:2px solid #bbb;display:flex;align-items:center;justify-content:space-between;padding:0 8px;font-size:11px;color:#aaa}
.select i{width:17px;height:17px;background:var(--blue);display:flex;align-items:center;justify-content:center}
.search-btn{position:absolute;left:670px;top:60px;width:90px;height:30px;border:1px solid #8fc3ec;color:#fff;font:400 15px Arimo,Arial,sans-serif;display:flex;align-items:center;justify-content:center;gap:6px}

.card{top:467px;width:161px;height:202px;background:var(--panel);box-shadow:0 1px 2px rgba(0,0,0,.15)}
.card h3{height:30px;color:#fff;font-size:19px;font-weight:700;display:flex;align-items:center;gap:8px;padding-left:8px}
.card h3 .ico{width:16px;height:18px;background:rgba(255,255,255,.85)}
.card ul{list-style:none;padding:8px 8px 0 10px}
.card li{font-size:11.2px;line-height:18px;color:#555;padding-left:8px;position:relative}
.card li:before{content:"•";position:absolute;left:0}
.c-orange h3{background:var(--orange)}
.c-pink h3{background:var(--pink)}
.c-green h3{background:var(--green)}

.ad{left:619px;top:468px;width:188px;height:187px;background:var(--green);color:#fff;font-size:24px;font-weight:700;display:flex;align-items:center;justify-content:center;text-align:center;line-height:1.2;letter-spacing:1px}

.welcome-bg{left:170px;top:770px;width:340px;height:220px;background:radial-gradient(ellipse,rgba(150,140,130,.18),rgba(243,243,243,0) 70%)}
.welcome{left:76px;top:686px;width:502px}
.welcome h1{font-size:20px;color:#666;font-weight:700;display:flex;align-items:baseline;gap:10px;margin-bottom:10px}
.welcome h1 span{font-size:37px;color:var(--steel)}
.puppy{float:left;width:68px;height:76px;margin:0 22px 4px 8px;background:radial-gradient(ellipse,#c79a5a 0%,#e3c79a 55%,rgba(243,243,243,0) 75%)}
.welcome p{font-size:8.6px;line-height:16.5px;color:#666}
.welcome a{color:var(--green);font-size:8.6px;margin-left:8px}

.news{left:610px;top:688px;width:216px}
.news-head{border-top:3px solid var(--orange);background:#fff;height:38px;padding-left:9px;display:flex;align-items:center;font-size:19px;color:#333}
.article{background:#fff;margin-top:4px;height:86px;border-bottom:1px solid #ccc;position:relative}
.article h4{background:#e8e8e8;height:22px;font-size:15px;color:var(--green);padding-left:8px;display:flex;align-items:center;font-weight:700}
.article h4 i{position:absolute;right:10px;top:4px;width:10px;height:15px;background:#c9a67a}
.article p{font-size:8px;line-height:11px;color:#555;padding:5px 8px 0 8px}
.article .more{position:absolute;right:14px;bottom:3px;background:var(--blue);color:#fff;font-size:7.5px;padding:2px 5px}

.footer-band{left:0;top:1018px;width:900px;height:32px;background:var(--footer)}
.fcol{top:1024px}
.fcol h5{font-size:16px;font-weight:400;color:#333;margin-left:6px;height:26px}
.fcol ul{list-style:none;margin-top:8px}
.fcol li{font-size:8.6px;line-height:18px;color:#555;padding-left:10px;position:relative}
.fcol li:before{content:"•";position:absolute;left:0;color:#999}
.social{left:676px;top:1024px;display:flex;align-items:center;gap:4px;font-size:11px;color:#333;font-style:italic}
.social span.sq{width:20px;height:20px;border-radius:3px}
.foot-logo{left:661px;top:1061px;width:163px;height:82px;background:#000;border:2px solid #fff;display:flex;align-items:center;justify-content:center;gap:8px}
.copy{left:0;top:1166px;width:900px;height:34px;background:var(--footer);display:flex;align-items:center;justify-content:center;font-size:8.6px;color:#555}
</style>
</head>
<body>

<div class="abs logo"><span class="logo-mark"></span><span class="logo-name">Cover Compare Quizzo</span></div>

<nav class="abs nav">
  <span class="active-bar"></span>
  <a href="#">Home</a><a href="#">Policies</a><a href="#">Glossary</a><a href="#">Fact Sheets</a><a href="#">Survey Reports</a><a href="#">News &amp; Comment</a>
</nav>

<div class="abs hero-text cond">
  <div class="l1">We do not <b>sell pet insurance…</b></div>
  <div class="l2">or receive commission</div>
  <div class="l3">from pet insurance companies...</div>
</div>
<div class="abs hero-photo" role="img" aria-label="Photo of two basset hound puppies sitting side by side"></div>
<div class="abs slider-arrows">
  <span><svg width="8" height="14"><path d="M7 1L1 7l6 6" stroke="#fff" fill="none" stroke-width="1.5"/></svg></span>
  <span><svg width="8" height="14"><path d="M1 1l6 6-6 6" stroke="#fff" fill="none" stroke-width="1.5"/></svg></span>
</div>

<section class="abs lookup">
  <h2 class="cond"><span class="lookup-icon"></span>Check out a Policy</h2>
  <div class="select" style="left:76px"><div>-Select Company-<i><svg width="9" height="6"><path d="M0 0h9L4.5 6z" fill="#fff"/></svg></i></div></div>
  <div class="select" style="left:372px"><div>-Select Policy-<i><svg width="9" height="6"><path d="M0 0h9L4.5 6z" fill="#fff"/></svg></i></div></div>
  <div class="search-btn">Search <svg width="20" height="20"><circle cx="12" cy="8" r="6" fill="#cfe6f7" stroke="#e8a93a" stroke-width="2"/><path d="M8 12L2 18" stroke="#e8a93a" stroke-width="3"/></svg></div>
</section>

<div class="abs card c-orange" style="left:74px">
  <h3 class="cond"><span class="ico"></span>Menu List</h3>
  <ul><li>Policy Files</li><li>Policy Search</li><li>Fact Sheets</li><li>Policy Listing by Type</li><li>Claims Survey</li><li>2013 Price Survey Report</li></ul>
</div>
<div class="abs card c-pink" style="left:246px">
  <h3 class="cond"><span class="ico"></span>Popular Reviews</h3>
  <ul><li>Pet Insurance - an introduction</li><li>Pet Insurance Policies - Know Your</li><li>Terms</li><li>Vet Fees - Policy Types</li><li>Using Price Comparison Engines</li><li>Common Policy Terms</li></ul>
</div>
<div class="abs card c-green" style="left:417px">
  <h3 class="cond"><span class="ico"></span>Latest Reviews</h3>
  <ul><li>Lorem Ipsum Doller.</li><li>Lorem Ipsum Doller.</li><li>Lorem Ipsum Doller.</li><li>Lorem Ipsum Doller.</li><li>Lorem Ipsum Doller.</li><li>Lorem Ipsum Doller.</li></ul>
</div>
<div class="abs ad cond">Advertising<br>Spance</div>

<div class="abs welcome-bg" role="img" aria-label="Faint background photo of a basset hound"></div>
<section class="abs welcome">
  <h1 class="cond">Welcome to <span>COVER COMPARE QUIZZO</span></h1>
  <div class="puppy" role="img" aria-label="Photo of a golden puppy"></div>
  <p>Lorem ipsum dolor sit amet, consectetur adipiscing elit. Donec a massa vel quam tempus semper non vel at felis tincidunt interdum. Vestibulum justo nisl, ultricies id aliquet a, ultrices vel risus. In ullamcorper rhonc ue ac nisl libero. Nullam cursus dui sed urna consectetur in pharetra ligula accumsan. Suspendisse neque icula a, scelerisque id tortor. Lorem ipsum dolor sit amet, consectetur adipiscing elit. Donec a massa vel Lorem ipsum dolor sit amet, consectetur adipiscing elit. Donec a massa vel quam tempus semper non vel sapien. Morbi vel erat at felis tincidunt interdum. Vestibulum justo nisl, ultricies id aliquet a, ultrices vel risus. In ullamcorper rhoncus convallis. Pellentesq ue ac nisl libero. Nullam cursus dui sed urna consectetur in pharetra ligula accumsan. Suspendisse neque metus, placerat vel veh icula a, scelerisque id tortor. Lorem ipsum dolor sit amet, consectetur adipiscing elit. Donec a massa vel quam tempus semper non vel sapien. Morbi vel erat.<br>at felis tincidunt interdum. Vestibulum justo nisl, ultricies id aliquet a, ultrices vel risus. In ullamcorper rhoncus convallis. Pellentesq ue ac nisl libero. Nullam cursus dui sed urna consectetur in pharetra ligula accumsan. Suspendisse neque metus, placerat vel veh icula a, scelerisque id tortor. <a href="#">more...</a></p>
</section>

<section class="abs news">
  <div class="news-head cond">News and Comment Section</div>
  <div class="article"><h4 class="cond">Article 1<i></i></h4><p>Lorem ipsum dolor sit amet, consectetur adipiscing elit. Curabitur eros lorem, ultricies non vestibulum eu facilisis a quam. Donec ac tellus et erat adipiscing vehicula quis in nisi</p><span class="more">more...</span></div>
  <div class="article"><h4 class="cond">Article 1<i></i></h4><p>Lorem ipsum dolor sit amet, consectetur adipiscing elit. Curabitur eros lorem, ultricies non vestibulum eu facilisis a quam. Donec ac tellus et erat adipiscing vehicula quis in nisi</p><span class="more">more...</span></div>
  <div class="article"><h4 class="cond">Article 1<i></i></h4><p>Lorem ipsum dolor sit amet, consectetur adipiscing elit. Curabitur eros lorem, ultricies non vestibulum eu facilisis a quam. Donec ac tellus et erat adipiscing vehicula quis in nisi</p><span class="more">more...</span></div>
</section>

<div class="abs footer-band"></div>
<div class="abs fcol" style="left:76px"><h5 class="cond">Menu</h5><ul><li>Home</li><li>Policies</li><li>Glossary</li><li>Fact Sheets</li><li>Survey Reports</li><li>News &amp; Comment</li></ul></div>
<div class="abs fcol" style="left:233px"><h5 class="cond">Menu List</h5><ul><li>Policy Files</li><li>Policy Search</li><li>Fact Sheets</li><li>Policy Listing by Type</li><li>Claims Survey</li><li>2013 Price Survey Report</li></ul></div>
<div class="abs fcol" style="left:386px"><h5 class="cond" style="margin-left:2px">Popular Reviews</h5><ul><li>Pet Insurance - an introduction</li><li>Pet Insurance Policies - Know Your</li><li>Terms</li><li>Vet Fees - Policy Types</li><li>Using Price Comparison Engines</li><li>Common Policy Terms</li></ul></div>
<div class="abs social">Join With Us: <span class="sq" style="background:#3b5ea8;margin-left:4px"></span><span class="sq" style="background:#39a9e0"></span><span class="sq" style="background:#f0a030"></span></div>
<div class="abs foot-logo"><span class="logo-mark"></span><span class="logo-name">Cover Compare Quizzo</span></div>
<div class="abs copy">COVER COMPARE QUIZZO 2013 © All Rights Reserved</div>

</body>
</html>
```